Postcard Design

We are Thessaly Pages based on Oxford, UK. We sell rare and collectible books and we want to include an attractive postcard with the order. This is seen as having several functions: a thank you for buying from us, a functional item that can be used as a book mark, a reminder of how to contact us and browse our ever-changing stock at www.thessalypages.co.uk (please note the website is off-line at the moment for some major improvements).

We like clean and simple designs. We pride ourselves on the quality of our stock, our honest appraisals of the condition of our books and our no-quibble guarantee - if the buyer is unhappy for any reason we will give a full refund (including postage) on safe return of the item.

Requirements
Must have
• website address (www.thessalypages.co.uk)

```html
<!DOCTYPE html>
<html lang="en">
<head>
<meta charset="utf-8">
<title>Thessaly Pages – Postcard</title>
<link rel="stylesheet" href="https://fonts.googleapis.com/css2?family=Sorts+Mill+Goudy&family=Cormorant+Garamond:wght@700&family=Open+Sans:wght@300&display=swap">
<style>
  :root {
    --paper: #ffffff;
    --ribbon: #9b2b2a;
    --ribbon-edge: #e7c9c6;
    --ink: #2a2420;
    --rule: #8a8a8a;
    --label: #8c8c8c;
    --frame: #9a9a9a;
  }
  * { margin: 0; padding: 0; box-sizing: border-box; }
  html, body { width: 1200px; height: 924px; overflow: hidden; background: var(--paper); }
  .postcard { position: relative; width: 1200px; height: 924px; background: var(--paper); }

  .shelf-photo {
    position: absolute; left: 0; top: 40px; width: 585px; height: 345px;
    background: linear-gradient(90deg,
      #2f4a48 0%, #3b5a6a 18%, #1f2a2a 32%, #b07a3c 42%, #9c6a34 52%,
      #8c3a34 64%, #7a2e2c 72%, #4e6a4c 84%, #5f7a58 100%);
  }

  .headline-ribbon { position: absolute; left: 0; top: 211px; width: 600px; height: 116px; }
  .headline {
    position: absolute; left: 45px; top: 222px; width: 520px;
    font-family: "Cormorant Garamond", "Sorts Mill Goudy", serif; font-weight: 700;
    font-size: 37px; line-height: 48px; color: var(--paper);
  }

  .selling-points {
    position: absolute; left: 45px; top: 406px; width: 533px; list-style: none;
    font-family: "Sorts Mill Goudy", serif; font-size: 22px; line-height: 37.5px;
    color: var(--ink); text-align: justify; letter-spacing: 0.2px;
  }
  .selling-points li { position: relative; margin-bottom: 8px; }
  .selling-points li::before {
    content: ""; position: absolute; left: -14px; top: 15px;
    width: 7px; height: 7px; border-radius: 50%; background: var(--ribbon);
  }

  .brand-plate {
    position: absolute; left: 62px; top: 806px; width: 470px; height: 88px;
    background: var(--ribbon); transform: rotate(0.6deg);
    box-shadow: 3px 4px 6px rgba(0,0,0,0.35);
    text-align: center; color: var(--paper); font-family: "Sorts Mill Goudy", serif;
  }
  .brand-name { font-size: 40px; line-height: 46px; padding-top: 2px; }
  .brand-url { font-family: "Cormorant Garamond", serif; font-weight: 700; font-size: 27px; line-height: 30px; }

  .postage-box {
    position: absolute; left: 939px; top: 44px; width: 200px; height: 200px;
    border: 2px solid var(--frame);
    font-family: "Open Sans", sans-serif; font-weight: 300; font-size: 32px;
    line-height: 42px; color: var(--label); text-align: center; padding-top: 70px;
  }
  .address-label {
    position: absolute; left: 773px; top: 362px;
    font-family: "Open Sans", sans-serif; font-weight: 300; font-size: 32px; color: var(--label);
  }
  .address-line { position: absolute; height: 0; border-top: 1.5px solid var(--rule); }
  .line-long { left: 686px; width: 479px; }
  .line-short { left: 696px; width: 459px; }
</style>
</head>
<body>
<main class="postcard">
  <div class="shelf-photo" role="img" aria-label="Photograph of a row of antique leather-bound books on a shelf"></div>

  <svg class="headline-ribbon" viewBox="0 0 600 116" aria-hidden="true">
    <polygon points="0,2 597,2 572,58 597,114 0,114" fill="var(--ribbon)"/>
    <polyline points="0,8 585,8 562,58 585,108 0,108" fill="none" stroke="var(--ribbon-edge)" stroke-width="1.5"/>
  </svg>
  <h1 class="headline">We have Rare Collection of limited Editions Books.</h1>

  <ul class="selling-points">
    <li>Our books represent the best and most interesting of their books from among the millions of titles available on Thessaly Pages.</li>
    <li>We sale good condition books which comes with our no quibble guarantee. if the buyer is unhappy for any reason we will give a full refund including postage on safe return of the item.</li>
    <li>We invite you to explore and learn more about the categories, our ever changing stocks and exclusive offers on collectable books.</li>
  </ul>

  <div class="brand-plate">
    <div class="brand-name">Thessaly Pages</div>
    <div class="brand-url">www.thessalypages.co.uk</div>
  </div>

  <div class="postage-box">Postage<br>Area</div>
  <div class="address-label">Address Area</div>
  <div class="address-line line-long" style="top:435px"></div>
  <div class="address-line line-short" style="top:498px"></div>
  <div class="address-line line-long" style="top:560px"></div>
  <div class="address-line line-short" style="top:623px"></div>
</main>
</body>
</html>
```